The Copper Hour ebook cover for Desmond Okafor Whitley

I need an ebook cover/jpeg that depicts a Middle-Eastern desert and sky. The cover must be very elegant and very austere, the simpler the better.
Toward the top, the text will read: The Copper Hour
Directly below the title will read: Corvin Teague
The dimensions for the cover should be 2560 pixels (height) and 1600 pixels (width.)

Target Market(s)

Readers of serious magical realism and/or fantasy literature with a serious literary element.

Font styles to use
Serif

Requirements
Must have
• My ebook cover MUST be a painting or illustration depicting a very austere Middle-Eastern desert and desert sky. Must be elegant and austere. The lettering of the title and author name must blend in beautifully with the image--just like fine books in a bookstore. Title must appear at the top: The Copper Hour. The author's name must appear below title and read: Corvin Teague. Dimensions must be 2560 pixels (height) by 1600 pixels (width)
Nice to have
• A very austere desert on the bottom and a sad elegant sky above.
Should not have
• My ebook cover should not have a spine or a back. I just need an ebook cover of the dimensions stated above.

```html
<!DOCTYPE html>
<html lang="en">
<head>
<meta charset="utf-8">
<title>The Copper Hour — Ebook Cover</title>
<link rel="stylesheet" href="https://fonts.googleapis.com/css2?family=Crimson+Text:wght@400&display=swap">
<style>
  :root {
    --backdrop: #ece6d8;
    --sky-deep: #0b2640;
    --sky-mid: #123654;
    --sky-glow: #1d4a66;
    --sand: #93a79f;
    --sand-shade: #86998f;
    --title-ink: #9eb0aa;
    --author-ink: #0f2a44;
  }
  * { margin: 0; padding: 0; box-sizing: border-box; }
  html, body {
    width: 1200px;
    height: 864px;
    overflow: hidden;
    background: var(--backdrop);
  }
  .stage {
    width: 1200px;
    height: 864px;
    display: flex;
    align-items: center;
    justify-content: center;
  }
  .cover {
    position: relative;
    width: 500px;
    height: 800px;
    overflow: hidden;
    background: var(--sky-deep);
    box-shadow: 0 6px 24px rgba(40, 30, 10, 0.18);
  }
  .cover__sky {
    position: absolute;
    inset: 0;
    background:
      radial-gradient(ellipse 55% 35% at 38% 42%, var(--sky-glow) 0%, rgba(29, 74, 102, 0) 70%),
      linear-gradient(180deg, var(--sky-deep) 0%, var(--sky-mid) 55%, var(--sky-deep) 100%);
  }
  .cover__dune {
    position: absolute;
    left: 0;
    bottom: 0;
    width: 500px;
    height: 800px;
  }
  .cover__title {
    position: absolute;
    top: 258px;
    right: 14px;
    font-family: "Crimson Text", Georgia, serif;
    font-weight: 400;
    font-size: 44px;
    letter-spacing: 0.5px;
    color: var(--title-ink);
    white-space: nowrap;
  }
  .cover__author {
    position: absolute;
    top: 634px;
    right: 22px;
    font-family: "Crimson Text", Georgia, serif;
    font-weight: 400;
    font-size: 28px;
    letter-spacing: 0.3px;
    color: var(--author-ink);
    white-space: nowrap;
  }
</style>
</head>
<body>
  <main class="stage">
    <section class="cover" aria-label="Ebook cover: The Copper Hour by Corvin Teague">
      <div class="cover__sky" role="img" aria-label="Deep blue night sky scattered with stars and a faint Milky Way"></div>
      <svg class="cover__dune" viewBox="0 0 500 800" role="img" aria-label="Pale speckled desert dune beneath the night sky">
        <defs>
          <linearGradient id="sand-tone" x1="0" y1="0" x2="0" y2="1">
            <stop offset="0" stop-color="var(--sand)"/>
            <stop offset="1" stop-color="var(--sand-shade)"/>
          </linearGradient>
        </defs>
        <path d="M0 478 C 60 470, 110 470, 170 482 C 260 500, 330 560, 410 595 C 450 612, 480 620, 500 624 L 500 800 L 0 800 Z" fill="url(#sand-tone)"/>
      </svg>
      <h1 class="cover__title">The Copper Hour</h1>
      <p class="cover__author">Corvin Teague</p>
    </section>
  </main>
</body>
</html>
```